UPDATE: I have uploaded the selected logo from the other contest, please use it in your designs.

I have a logo design contest as well so not sure how ArtHive handles that. They should integrate at some point. I will describe the overall theme with the logo description. See it for details.

The business card side of it would just build on that same theme.

Target Market(s)

8-40

Industry/Entity Type

Business

Contact Information for Business Card

FirstName LastName
Email

Logo Text

VelMarin

Font styles to use
Sans Serif

Requirements
Must have
• the url VelMarin.com somewhere in it.

```html
<!DOCTYPE html>
<html lang="en">
<head>
<meta charset="utf-8">
<title>VelMarin Business Card</title>
<link rel="stylesheet" href="https://fonts.googleapis.com/css2?family=Exo+2:wght@600;700&display=swap">
<style>
  :root {
    --backdrop: #e6e8eb;
    --card-blue: #1a63a8;
    --card-blue-deep: #0f4f8f;
    --navy-line: #173a66;
    --lime: #8cc63f;
    --paper: #ffffff;
    --brand-blue: #1c6fb8;
    --text-light: #ffffff;
  }
  * { margin: 0; padding: 0; box-sizing: border-box; }
  html, body {
    width: 1200px;
    height: 840px;
    overflow: hidden;
    background: var(--backdrop);
  }
  .canvas {
    position: relative;
    width: 1200px;
    height: 840px;
  }
  .business-card {
    position: absolute;
    left: 100px;
    top: 134px;
    width: 1000px;
    height: 572px;
    overflow: hidden;
    box-shadow: 0 10px 30px rgba(0, 0, 0, 0.18);
    font-family: "Exo 2", sans-serif;
  }
  .card-bands {
    position: absolute;
    inset: 0;
    display: block;
  }
  .brand-name {
    position: absolute;
    left: 300px;
    top: 80px;
    width: 660px;
    text-align: center;
    font-size: 124px;
    font-weight: 700;
    line-height: 1;
    letter-spacing: 6px;
    color: var(--brand-blue);
  }
  .contact {
    position: absolute;
    left: 52px;
    top: 368px;
    font-variant: small-caps;
  }
  .contact-name {
    font-size: 44px;
    font-weight: 700;
    color: var(--lime);
    letter-spacing: 1px;
    margin-bottom: 14px;
  }
  .contact-line {
    font-size: 28px;
    font-weight: 600;
    color: var(--text-light);
    letter-spacing: 1px;
    line-height: 1.45;
  }
</style>
</head>
<body>
<main class="canvas">
  <section class="business-card">
    <svg class="card-bands" viewBox="0 0 1000 572" aria-hidden="true">
      <defs>
        <linearGradient id="card-blue-fill" x1="0" y1="0" x2="1" y2="1">
          <stop offset="0" stop-color="var(--card-blue)"/>
          <stop offset="1" stop-color="var(--card-blue-deep)"/>
        </linearGradient>
      </defs>
      <rect class="card-base" width="1000" height="572" fill="url(#card-blue-fill)"/>
      <polygon class="lime-band" points="66,0 1000,0 1000,356 250,356 66,184" fill="var(--lime)"/>
      <polygon class="blue-gap" points="88,0 1000,0 1000,334 260,334 88,174" fill="var(--card-blue)"/>
      <polygon class="navy-line" points="108,0 1000,0 1000,314 266,314 108,166" fill="var(--navy-line)"/>
      <polygon class="white-panel" points="120,0 1000,0 1000,302 272,302 120,160" fill="var(--paper)"/>
    </svg>
    <div class="brand-name">VelMarin</div>
    <div class="contact">
      <p class="contact-name">Mira Dalton</p>
      <p class="contact-line">info@VelMarin.com</p>
      <p class="contact-line">www.VelMarin.com</p>
    </div>
  </section>
</main>
</body>
</html>
```